spanish seafood rice meal

Hi, I need a design for Spanish seafood rice meal. The aimed market is North America and European. Please use the picture of my product I uploaded, it can be the cover of packaging. Also I upload a sample I found from supermarket. Please use simple colour. The size is 220mm*155mm*40mm. Thanks.

```html
<!DOCTYPE html>
<html lang="en">
<head>
<meta charset="UTF-8">
<title>Fresh Cooked Paella – Front Panel</title>
<link rel="stylesheet" href="https://fonts.googleapis.com/css2?family=Bodoni+Moda:wght@500;700&family=Great+Vibes&family=Montserrat:wght@600&family=Playfair+Display:wght@700&display=swap">
<style>
  :root {
    --bg: #d9d9d9;
    --saffron: #eeaa22;
    --paprika: #c0121a;
    --cream: #ffffff;
    --ink: #1a1412;
    --plate: #2a2a2c;
    --rice: #e8b631;
  }
  * { box-sizing: border-box; margin: 0; padding: 0; }
  html, body { width: 1200px; height: 840px; overflow: hidden; }
  body { background: var(--bg); position: relative; }

  .pack-front {
    position: absolute;
    left: 330px; top: 40px;
    width: 540px; height: 760px;
    background: var(--saffron);
    overflow: hidden;
    box-shadow: 0 20px 40px rgba(0,0,0,0.18);
  }

  .brand-box {
    position: absolute;
    left: 160px; top: 38px;
    width: 210px; height: 92px;
    background: var(--cream);
    display: flex; align-items: center; justify-content: center;
  }
  .brand-name {
    font-family: "Bodoni Moda", serif;
    font-weight: 500;
    font-size: 38px;
    letter-spacing: 8px;
    padding-left: 8px;
    color: var(--paprika);
  }

  .badge { position: absolute; overflow: visible; }
  .badge-heat { left: 414px; top: 30px; width: 110px; height: 90px; }
  .badge-cold { left: 22px; top: 128px; width: 110px; height: 90px; }
  .badge text {
    font-family: "Montserrat", sans-serif;
    font-weight: 600;
    font-size: 9px;
    letter-spacing: 0.3px;
    fill: var(--paprika);
  }

  .tagline {
    position: absolute;
    left: 120px; right: 20px; top: 140px;
    text-align: center;
    font-family: "Great Vibes", cursive;
    font-weight: 400;
    font-size: 56px;
    line-height: 1.2;
    color: var(--ink);
  }

  .title-band {
    position: absolute;
    left: 0; top: 222px;
    width: 100%; height: 150px;
    background: var(--paprika);
    text-align: center;
  }
  .product-name {
    font-family: "Bodoni Moda", serif;
    font-weight: 500;
    font-size: 84px;
    line-height: 1;
    letter-spacing: 28px;
    padding-left: 28px;
    color: var(--cream);
    margin-top: 20px;
  }
  .product-sub {
    font-family: "Montserrat", sans-serif;
    font-weight: 600;
    font-size: 20px;
    letter-spacing: 2px;
    color: var(--saffron);
    margin-top: 14px;
  }

  .ingredients {
    position: absolute;
    left: 0; right: 0; top: 388px;
    text-align: center;
    font-family: "Playfair Display", serif;
    font-weight: 700;
    font-size: 15px;
    line-height: 1.25;
    letter-spacing: 1px;
    color: var(--ink);
  }

  .hero-photo {
    position: absolute;
    left: -30px; top: 450px;
    width: 600px; height: 380px;
    border-radius: 50% 50% 0 0 / 40% 40% 0 0;
    background:
      radial-gradient(ellipse at 50% 50%, var(--rice) 0%, #d9a42c 50%, #8a6a2a 70%, var(--plate) 78%);
  }
</style>
</head>
<body>
  <main class="pack-front">
    <div class="brand-box"><span class="brand-name">LOGO</span></div>

    <svg class="badge badge-heat" viewBox="0 0 110 90" aria-label="Heat and serve">
      <defs><path id="arc-heat" d="M17,52 A38,38 0 0,1 93,52"/></defs>
      <text><textPath href="#arc-heat" startOffset="50%" text-anchor="middle">HEAT &amp; SERVE</textPath></text>
      <g fill="none" stroke="var(--paprika)" stroke-width="2.2" stroke-linecap="round">
        <path d="M39 56 H69 Q69 68 54 68 Q39 68 39 56 Z"/>
        <path d="M69 58 L83 54"/>
        <path d="M49 50 Q45 44 50 38 Q51 44 54 42 Q53 36 58 32 Q59 42 62 44 Q63 48 59 50"/>
      </g>
    </svg>

    <svg class="badge badge-cold" viewBox="0 0 110 90" aria-label="Keep refrigerated">
      <defs><path id="arc-cold" d="M12,58 A43,43 0 0,1 98,58"/></defs>
      <text><textPath href="#arc-cold" startOffset="50%" text-anchor="middle">KEEP REFRIGERATED</textPath></text>
      <g stroke="var(--paprika)" stroke-width="2.2" stroke-linecap="round" fill="none">
        <line x1="55" y1="44" x2="55" y2="72"/>
        <line x1="43" y1="51" x2="67" y2="65"/>
        <line x1="43" y1="65" x2="67" y2="51"/>
        <path d="M51 47 L55 51 L59 47 M51 69 L55 65 L59 69"/>
      </g>
    </svg>

    <h2 class="tagline">Fresh Cooked</h2>

    <section class="title-band">
      <h1 class="product-name">PAELLA</h1>
      <p class="product-sub">SPANISH SEAFOOD RICE MEAL</p>
    </section>

    <p class="ingredients">FISH, MUSSELS, CLAMS, SHRIMPS, SCALLOPS<br>AND SQUID WITH SAFFRON RICE</p>

    <div class="hero-photo" role="img" aria-label="Photo of seafood paella with shrimps, mussels, squid and scallops on saffron rice in a dark pan"></div>
  </main>
</body>
</html>
```